Silverleaf Rise Accounting Program

size of ad Full: 7” x 9.6”
1- this is for a ladies program so it should appeal to women.
2-however, I do not want any pictures of people in this ad.
3-all the text should be seen and not covered over by graphics.
4-It should be an ad that will draw people's attention and people should look at it and say it looks nice I want to see that ad.
5-I have put all the instructions in yellow in the file below.
6-please leave 1 inch for the footer .
good luck with this project

• no picture or vector of people.

```html
<!DOCTYPE html>
<html lang="en">
<head>
<meta charset="UTF-8">
<title>Silverleaf Rise Accounting Program – Open House Flyer</title>
<link href="https://fonts.googleapis.com/css2?family=Montserrat:wght@500;600;700;800&display=swap" rel="stylesheet">
<style>
  :root {
    --red: #e31e26;
    --charcoal: #3a3a3c;
    --ink: #2b2b2d;
    --white: #ffffff;
  }
  * { margin: 0; padding: 0; box-sizing: border-box; }
  html, body { width: 928px; height: 1200px; overflow: hidden; background: var(--white); }
  body { font-family: "Montserrat", Arial, sans-serif; }

  .flyer { position: relative; width: 928px; height: 1200px; background: var(--white); overflow: hidden; }

  .hero { position: absolute; left: 0; top: 0; width: 928px; height: 580px; }
  .hero svg { display: block; }

  .hero-title {
    position: absolute; right: 52px; top: 386px;
    text-align: right; color: var(--white);
    text-shadow: 2px 3px 4px rgba(0,0,0,0.35);
  }
  .hero-title .line { display: block; font-weight: 500; font-size: 53px; line-height: 53px; letter-spacing: 1px; }
  .hero-title .subject { display: block; font-weight: 800; font-size: 67px; line-height: 72px; letter-spacing: 0.5px; }

  .tagline-band {
    position: absolute; left: 0; top: 580px; width: 928px; height: 94px;
    background: var(--charcoal); color: var(--white);
    display: flex; align-items: center; justify-content: center;
    text-align: center; font-weight: 700; font-size: 21px; line-height: 29px;
  }

  .advantage {
    position: absolute; left: 34px; top: 674px; width: 455px; height: 379px;
    background: var(--red); color: var(--white); padding: 29px 0 0 44px;
  }
  .advantage h2 { font-weight: 800; font-size: 48px; line-height: 51px; letter-spacing: 0.5px; margin-bottom: 12px; }
  .advantage ul { list-style: none; }
  .advantage li { position: relative; padding-left: 25px; font-weight: 700; font-size: 26px; line-height: 36px; white-space: nowrap; }
  .advantage li::before {
    content: ""; position: absolute; left: 2px; top: 13px;
    width: 11px; height: 11px; border-radius: 50%; background: var(--white);
  }

  .event-details { position: absolute; left: 558px; top: 758px; width: 350px; color: var(--ink); }
  .detail { border-left: 3px solid var(--red); padding-left: 13px; }
  .detail-open { font-weight: 600; font-size: 22px; line-height: 28px; padding-top: 13px; padding-bottom: 13px; margin-bottom: 22px; }
  .detail-date { font-weight: 600; font-size: 23px; line-height: 28px; padding-left: 17px; margin-bottom: 32px; }
  .detail-note { font-weight: 500; font-size: 18.5px; line-height: 22px; }

  .contact-bar {
    position: absolute; left: 34px; top: 1079px; width: 860px; height: 93px;
    background: var(--charcoal); color: var(--white); text-align: center; padding-top: 13px;
  }
  .contact-bar .prompt { font-weight: 500; font-size: 20px; line-height: 24px; }
  .contact-bar .channels { font-weight: 700; font-size: 32px; line-height: 42px; letter-spacing: 0.5px; }
</style>
</head>
<body>
<main class="flyer">
  <section class="hero">
    <svg width="928" height="580" viewBox="0 0 928 580" role="img" aria-label="Photo of an accountant working at a desk with a laptop, calculator and financial charts">
      <defs>
        <linearGradient id="photoTone" x1="0" y1="0" x2="1" y2="1">
          <stop offset="0" stop-color="#6b6e74"/>
          <stop offset="0.45" stop-color="#b8b4ad"/>
          <stop offset="1" stop-color="#e2ddd3"/>
        </linearGradient>
        <linearGradient id="redWash" x1="0" y1="1" x2="1" y2="0">
          <stop offset="0" stop-color="#e31e26"/>
          <stop offset="1" stop-color="#c8161e"/>
        </linearGradient>
      </defs>
      <rect width="928" height="580" fill="url(#photoTone)"/>
      <polygon points="0,580 928,200 928,580" fill="url(#redWash)" opacity="0.94"/>
    </svg>
    <h1 class="hero-title">
      <span class="line">A MASTER’S</span>
      <span class="line">DEGREE IN</span>
      <span class="subject">ACCOUNTING</span>
    </h1>
  </section>

  <p class="tagline-band">A STABLE, LUCRATIVE CAREER, WITH HIGH-PAYING,<br>FULL /PART TIME OPPORTUNITIES IN PRIVATE/PUBLIC COMPANIES</p>

  <section class="advantage">
    <h2>THE SRA JOB<br>PLACEMENT<br>ADVANTAGE</h2>
    <ul>
      <li>96% Placement Rate</li>
      <li>6 placement directors</li>
      <li>decades of relationships<br>with 100’s of firms</li>
    </ul>
  </section>

  <section class="event-details">
    <p class="detail detail-open">CONFERA OPEN HOUSE</p>
    <p class="detail detail-date">SUNDAY<br>JUNE 14, 02.00 PM</p>
    <p class="detail detail-note">GRADUATES HAVE BEEN<br>PLACED IN TOP COMPANIES<br>(FULL/PART TIME JOBS).</p>
  </section>

  <footer class="contact-bar">
    <p class="prompt">for a confera link / conference number / information</p>
    <p class="channels">info@silverleafrise.org or 555 014 2800x 111</p>
  </footer>
</main>
</body>
</html>
```